Promotional Flyer/Email Design - Cabling services for Broadcast and Audio Visual

We need a promotional flyer/email design to help launch our company, Velcor Lane. We provide cabling services for Broadcast Television and Audio Visual systems. Recent projects include major television events such as the Harrowmere Racquet Classic and Audio Visual/Entertainment systems for wealthy clients in their homes and on-board super yachts.

The flyer will be printed as single sided A5 and also be sent out in the body of a promotional email. It should feature the company logo along with a complementary colour scheme. It should have a clean finish with images that show the type of work we do (cabling and equipment installation) or the setting for these systems (tv studio, super yacht, cinema room, meeting room with projector etc.)

Services we offer are:

Broadcast/AV system design
On-site installation
Rack building
Pre-fabricated cable looms
Fibre optic installation

About the company:

Velcor Lane provide cabling services for Broadcast Television and Audio Visual systems. With over 15 years experience working in these industries we can help with every aspect of design, project managment, installation and maintenance. Our projects range from fibre optic cabling at major sports events to installing and commisioning bespoke control systems on some of the worlds largest super yachts.

Contact details:

To get a quote or discuss your project contact us now
Telephone: TBC
Email: info@velcor-lane.com
Website: www.velcor-lane.com
Address: TBC

Other information:

The company is based in London, UK. Our projects often take place in other countries with work taking place accross Europe and beyond.

We have a London based workshop for rack building and cable pre-fabrication.

Our website is www.velcor-lane.com

Images:

Images attached can be editted for use on the flyer or have ideas taken from them. Only the company logo is required to feature on the final design.

Target Market(s)

Business to business

Industry/Entity Type

It Company

Font styles to use
Sans Serif

Requirements
Must have
• Company logo
• List of services
• Contact details
Nice to have
• Image of cabling, home cinema room, super yacht, luxury home, outside broadcast truck, fibre optic equipment or cabling.

```html
<!DOCTYPE html>
<html lang="en">
<head>
<meta charset="utf-8">
<title>Velcor Lane – Flyer</title>
<link href="https://fonts.googleapis.com/css2?family=Montserrat:wght@400;500;600;700&family=Roboto:wght@400;900&display=swap" rel="stylesheet">
<style>
  :root {
    --backdrop: #c5d1d9;
    --paper: #ffffff;
    --ink: #4a4a4a;
    --ink-dark: #333333;
    --accent: #4a8fa3;
    --band: #5a78bb;
    --photo-deep: #0f2c2f;
    --photo-mid: #2f6e6c;
    --photo-light: #5f9c97;
    --white: #ffffff;
  }
  * { box-sizing: border-box; margin: 0; padding: 0; }
  html, body { width: 1200px; height: 700px; overflow: hidden; }
  body { background: var(--backdrop); font-family: "Montserrat", sans-serif; color: var(--ink); position: relative; }

  .flyer {
    position: absolute; left: 380px; top: 40px; width: 440px; height: 620px;
    background: var(--paper); overflow: hidden;
    box-shadow: 3px 4px 10px rgba(0,0,0,.25);
  }

  .hero-photo {
    position: absolute; left: 0; top: 0; width: 440px; height: 368px;
    background:
      radial-gradient(ellipse at 75% 55%, rgba(95,156,151,.55), transparent 60%),
      linear-gradient(100deg, var(--photo-deep) 0%, var(--photo-mid) 35%, var(--photo-light) 55%, var(--photo-mid) 75%, var(--photo-deep) 100%);
  }

  .region-tag { position: absolute; left: 48px; top: 44px; color: var(--white); }
  .region-tag::before { content: ""; display: block; width: 30px; height: 6px; background: var(--band); margin-bottom: 2px; }
  .region-tag span { font-weight: 700; font-size: 28px; line-height: 1; }

  .brand-mark {
    position: absolute; left: 193px; top: 220px; width: 42px; height: 36px;
    border: 2px solid var(--white); border-radius: 4px;
  }
  .brand-name {
    position: absolute; left: 0; width: 440px; top: 276px; text-align: center;
    color: var(--white); font-weight: 400; font-size: 33px; letter-spacing: 10px;
  }
  .brand-tagline {
    position: absolute; left: 0; width: 440px; top: 316px; text-align: center;
    color: var(--white); font-weight: 700; font-size: 7.5px; letter-spacing: 2.6px;
  }

  .headline {
    position: absolute; left: 48px; top: 384px;
    font-family: "Roboto", sans-serif; font-weight: 900; font-size: 47px;
    color: var(--ink); letter-spacing: 0.5px;
  }
  .rule { position: absolute; left: 48px; top: 441px; width: 340px; height: 1px; background: var(--ink); }

  .section-title { font-size: 12px; font-weight: 400; color: var(--ink-dark); margin-bottom: 3px; }
  .section-title strong { color: var(--accent); font-weight: 700; }

  .about { position: absolute; left: 48px; top: 451px; width: 180px; }
  .about p { font-size: 6.3px; line-height: 1.3; text-align: justify; color: var(--ink-dark); }

  .services { position: absolute; left: 240px; top: 451px; width: 170px; }
  .services ul { list-style: none; }
  .services li { font-size: 10.3px; line-height: 1.15; color: var(--ink-dark); font-weight: 500; }
  .services li::before { content: "•"; font-size: 8px; margin-right: 2px; }

  .cta {
    position: absolute; left: 0; width: 440px; top: 551px; text-align: center;
    font-size: 7.5px; font-weight: 700; color: var(--ink);
  }

  .footer-band { position: absolute; top: 560px; height: 60px; background: var(--band); }
  .footer-band.left { left: 0; width: 30px; }
  .footer-band.right { left: 405px; width: 35px; }

  .contact { position: absolute; display: flex; align-items: center; gap: 8px; font-size: 7.5px; color: var(--ink-dark); }
  .contact svg { width: 12px; height: 12px; fill: var(--ink-dark); flex: none; }

  .footer-brand {
    position: absolute; left: 300px; top: 584px;
    font-family: "Montserrat", sans-serif; font-weight: 700; font-size: 15px; color: var(--ink-dark);
  }
</style>
</head>
<body>
  <article class="flyer">
    <div class="hero-photo" role="img" aria-label="Photograph of broadcast equipment racks with dense cabling, tinted teal"></div>

    <div class="region-tag"><span>UK</span></div>
    <div class="brand-mark"></div>
    <h1 class="brand-name">VELCOR LANE</h1>
    <p class="brand-tagline">BROADCAST TELEVISION AND AUDIO VISUAL SYSTEMS</p>

    <h2 class="headline">HERE WE GO !</h2>
    <div class="rule"></div>

    <section class="about">
      <h3 class="section-title">ABOUT <strong>US</strong></h3>
      <p>Velcor Lane provide cabling services for Broadcast Television and Audio Visual systems. With over 15 years experience working in these industries we can help with every aspect of design, project managment, installation and maintenance. Our projects range from fibre optic cabling at major sports events to installing and commisioning bespoke control systems on some of the worlds largest super yachts.</p>
    </section>

    <section class="services">
      <h3 class="section-title">OUR <strong>SEVICES</strong></h3>
      <ul>
        <li>Broadcast/AV system design</li>
        <li>On-site installation</li>
        <li>Rack building</li>
        <li>Pre-fabricated cable looms</li>
        <li>Fibre optic installation</li>
      </ul>
    </section>

    <p class="cta">To get a quote or discuss your project contact us now</p>

    <div class="footer-band left"></div>
    <div class="footer-band right"></div>

    <div class="contact" style="left:46px; top:575px;">
      <svg viewBox="0 0 12 12"><path d="M6 0a4 4 0 0 0-4 4c0 3 4 8 4 8s4-5 4-8a4 4 0 0 0-4-4zm0 5.5a1.5 1.5 0 1 1 0-3 1.5 1.5 0 0 1 0 3z"/></svg>
      <span>London, UK</span>
    </div>
    <div class="contact" style="left:46px; top:596px;">
      <svg viewBox="0 0 12 12"><path d="M0 2h12v8H0z M1 3l5 3.5L11 3" fill="none" stroke="#333" stroke-width="1.2"/></svg>
      <span>info@velcor-lane.com</span>
    </div>
    <div class="contact" style="left:172px; top:573px;">
      <svg viewBox="0 0 12 12"><path d="M2.5 0.5l2 2.5-1.2 1.5c.8 1.7 2.2 3.1 3.9 3.9l1.5-1.2 2.5 2-1.3 2.3C5 11 1 7 .3 1.8z"/></svg>
      <span>(012) 555 0142</span>
    </div>
    <div class="contact" style="left:172px; top:594px;">
      <svg viewBox="0 0 12 12"><circle cx="6" cy="6" r="5.3" fill="none" stroke="#333" stroke-width="1.2"/><path d="M.7 6h10.6M6 .7c-3 3-3 7.6 0 10.6M6 .7c3 3 3 7.6 0 10.6" fill="none" stroke="#333" stroke-width="1"/></svg>
      <span>www.velcor-lane.com</span>
    </div>

    <div class="footer-brand">Velcor Lane</div>
  </article>
</body>
</html>
```